Architectural firm needs a graphic representation of our Master Planning process

We need an image to convey our 3-phase, 8-step Master Planning process that we utilize when designing plans for schools K-12. What we currently use looks very outdated in both the design and color scheme. We'd like an EPS created that can be scaled without distortion. The files I've attached show the current graphic and an instruction sheet which also contains our colors.

```html
<!DOCTYPE html>
<html lang="en">
<head>
<meta charset="utf-8">
<title>Master Planning Process</title>
<link href="https://fonts.googleapis.com/css2?family=Lilita+One&family=Roboto:wght@500&family=Tinos&display=swap" rel="stylesheet">
<style>
  :root {
    --purple: #5b3f98;
    --crimson: #9b1f35;
    --crimson-light: #b8344f;
    --teal: #21a093;
    --step-side: #3e4044;
    --base-gray: #9a9b9e;
    --footer: #54565a;
    --ink: #1c1c1c;
    --white: #ffffff;
  }
  html, body { margin: 0; padding: 0; overflow: hidden; }
  body { width: 927px; height: 1200px; background: var(--white); }
  .sheet { position: relative; width: 927px; height: 1200px; overflow: hidden; background: var(--white); }
  .process-graphic { position: absolute; left: 0; top: 0; }
  .label { font-family: "Lilita One", sans-serif; fill: var(--white); text-anchor: middle; }
  .caption {
    position: absolute; left: 40px; top: 902px; width: 847px; margin: 0;
    font-family: "Roboto", sans-serif; font-weight: 500; font-size: 18.5px;
    line-height: 30px; color: var(--ink); text-align: center;
  }
  .legend-band { position: absolute; left: 0; top: 1036px; width: 927px; height: 164px; background: var(--footer); }
  .legend-svg { position: absolute; left: 0; top: 0; }
  .legend-name { font-family: "Tinos", serif; font-size: 22px; fill: var(--white); }
</style>
</head>
<body>
<div class="sheet">
  <svg class="process-graphic" width="927" height="900" viewBox="0 0 927 900">
    <defs>
      <linearGradient id="teamBlend" x1="0" x2="1" y1="0" y2="0">
        <stop offset="0.3" stop-color="#9b1f35"/>
        <stop offset="0.45" stop-color="#5b3f98"/>
        <stop offset="0.6" stop-color="#5b3f98"/>
        <stop offset="0.78" stop-color="#21a093"/>
      </linearGradient>
      <radialGradient id="stepGlow" cx="0.5" cy="0.5" r="0.5">
        <stop offset="0" stop-color="#8a8a8e" stop-opacity="0.55"/>
        <stop offset="1" stop-color="#ffffff" stop-opacity="0"/>
      </radialGradient>
    </defs>

    <!-- School emblem -->
    <ellipse class="school-oval" cx="464" cy="240" rx="206" ry="94" fill="none" stroke="var(--purple)" stroke-width="2"/>
    <ellipse cx="464" cy="240" rx="200" ry="88" fill="var(--purple)"/>
    <rect class="school-building" role="img" aria-label="School building icon with flag" x="398" y="40" width="130" height="112" rx="4" fill="var(--purple)"/>
    <text class="label" x="464" y="200" font-size="40">SCHOOL</text>

    <!-- Consultants -->
    <path d="M214 292 L702 292 L690 312 L228 312 Z" fill="url(#teamBlend)"/>
    <rect x="214" y="218" width="232" height="82" rx="12" fill="var(--crimson)"/>
    <rect x="470" y="218" width="232" height="82" rx="12" fill="var(--teal)"/>
    <text class="label" x="330" y="250" font-size="25">ARCHITECTURAL</text>
    <text class="label" x="330" y="285" font-size="25">CONSULTANT</text>
    <text class="label" x="586" y="250" font-size="25">FUND RAISING</text>
    <text class="label" x="586" y="285" font-size="25">CONSULTANT</text>

    <!-- Visioning -->
    <rect x="326" y="310" width="274" height="52" fill="url(#teamBlend)"/>
    <text class="label" x="463" y="346" font-size="27" letter-spacing="8">VISIONING</text>
    <path d="M326 362 L600 362 L586 376 L340 376 Z" fill="var(--crimson-light)"/>

    <!-- Assessments -->
    <path d="M274 478 L653 478 L640 492 L287 492 Z" fill="var(--base-gray)"/>
    <rect x="274" y="376" width="166" height="102" fill="var(--crimson)"/>
    <rect x="486" y="376" width="167" height="102" fill="var(--crimson)"/>
    <path d="M440 376 L486 376 L486 478 L463 492 L440 478 Z" fill="var(--crimson-light)"/>
    <path d="M441 376 L485 376 L463 396 Z" fill="var(--white)"/>
    <text class="label" x="356" y="405" font-size="24">PHYSICAL</text>
    <text class="label" x="356" y="433" font-size="24">CONDITIONS</text>
    <text class="label" x="356" y="461" font-size="24">ASSESSMENT</text>
    <text class="label" x="570" y="405" font-size="24">SPACE</text>
    <text class="label" x="570" y="433" font-size="24">NEEDS</text>
    <text class="label" x="570" y="461" font-size="24">ASSESSMENT</text>
    <rect x="362" y="492" width="204" height="14" fill="var(--step-side)"/>

    <!-- Staircase -->
    <ellipse cx="463" cy="720" rx="310" ry="190" fill="url(#stepGlow)"/>

    <path d="M362 506 L566 506 L588 536 L342 536 Z" fill="var(--step-side)"/>
    <path d="M368 510 L560 510 L580 536 L348 536 Z" fill="var(--crimson)"/>
    <rect x="342" y="536" width="246" height="28" fill="var(--crimson)" stroke="var(--step-side)" stroke-width="3"/>
    <text class="label" x="465" y="559" font-size="22">PROBLEM DEFINED</text>

    <path d="M342 564 L588 564 L614 600 L314 600 Z" fill="var(--step-side)"/>
    <path d="M350 566 L580 568 L606 600 L320 600 Z" fill="var(--crimson)"/>
    <rect x="314" y="600" width="300" height="32" fill="var(--crimson)" stroke="var(--step-side)" stroke-width="3"/>
    <text class="label" x="464" y="626" font-size="23">IDENTIFY SOLUTIONS</text>

    <path d="M314 632 L614 632 L646 674 L282 674 Z" fill="var(--step-side)"/>
    <path d="M322 646 L606 646 L636 674 L290 674 Z" fill="url(#teamBlend)"/>
    <rect x="282" y="674" width="364" height="36" fill="url(#teamBlend)" stroke="var(--step-side)" stroke-width="3"/>
    <text class="label" x="464" y="701" font-size="23">ASSESS AND SELECT</text>

    <path d="M282 710 L646 710 L686 750 L242 750 Z" fill="var(--step-side)"/>
    <path d="M290 716 L638 718 L676 750 L250 750 Z" fill="var(--crimson)"/>
    <rect x="242" y="750" width="444" height="42" fill="var(--crimson)" stroke="var(--step-side)" stroke-width="3"/>
    <text class="label" x="464" y="782" font-size="23">COMPILE REPORT</text>

    <path d="M242 792 L686 792 L734 832 L194 832 Z" fill="var(--step-side)"/>
    <path d="M250 806 L678 806 L722 832 L204 832 Z" fill="url(#teamBlend)"/>
    <rect x="194" y="832" width="540" height="50" fill="url(#teamBlend)" stroke="var(--step-side)" stroke-width="3"/>
    <text class="label" x="464" y="868" font-size="23">IMPLEMENT PLAN</text>
  </svg>

  <p class="caption">Image above depicts a general outline of the process developed by K&amp;R and<br>used when conducting facilities master plans. The areas of responsibility are<br>shown by color yet the groups, especially the school and the architect, are<br>always working together towards the goal.</p>

  <div class="legend-band">
    <svg class="legend-svg" width="927" height="164" viewBox="0 0 927 164">
      <g class="legend-item">
        <path d="M118 36 L276 36 L322 104 L118 104 Z" fill="#1a1a1a"/>
        <path d="M118 40 L270 40 L312 104 L118 104 Z" fill="var(--purple)"/>
        <circle cx="96" cy="70" r="43" fill="#7a5fb5"/>
        <circle cx="96" cy="70" r="31" fill="var(--white)" role="img" aria-label="School building icon"/>
        <text class="legend-name" x="160" y="79">School</text>
      </g>
      <g class="legend-item">
        <path d="M400 36 L552 36 L598 104 L400 104 Z" fill="#1a1a1a"/>
        <path d="M400 40 L546 40 L588 104 L400 104 Z" fill="var(--teal)"/>
        <circle cx="372" cy="70" r="43" fill="#2cbaa0"/>
        <circle cx="372" cy="70" r="31" fill="var(--white)" role="img" aria-label="Hand holding a coin icon"/>
        <text class="legend-name" x="426" y="66">Fundraising</text>
        <text class="legend-name" x="426" y="92">Consultant</text>
      </g>
      <g class="legend-item">
        <path d="M680 36 L842 36 L888 104 L680 104 Z" fill="#1a1a1a"/>
        <path d="M680 40 L836 40 L878 104 L680 104 Z" fill="var(--crimson)"/>
        <circle cx="650" cy="74" r="43" fill="#c8203f"/>
        <circle cx="650" cy="74" r="31" fill="var(--white)" role="img" aria-label="Architect in hard hat icon"/>
        <text class="legend-name" x="712" y="82">Architect</text>
      </g>
    </svg>
  </div>
</div>
</body>
</html>
```